Give my personal webpage more appeal!

I need my CV website improved - drmeganholt.com.au.
I am using the template KESTREL from pagecraftly. i would like to keep the already existing theme but am open to suggestions.
Please focus on imagery, colour scheme, and textures to enhance the appeal and look of the page.
The content is there, but now I need a designer to improve the look of my page.
I need styling, royalty-free unique modern images to make the page professional, personal and friendly.
I work in healthcare, so I'm a people person.
I teach professionals and I treat a lot of families.

Target Market(s)

Parents, Professional Healthcare providers

Number of Pages Required

1 page

Font styles to use
Serif
Sans Serif

Requirements
Must have
• My face - image at the top, all the information already contained in it.
• Links to the websites I manage such as my blog.
• One Page website.
• All the information it already contains with the ability to have more.
• Ideally, we would keep the same format for the page although I'm happy to expand column and change the page's structure with in the theme template KESTREL.
Nice to have
• The current KESTREL template. I would like to keep the already existing theme but am open to suggestions.
Should not have
• Multiple pages.

```html
<!DOCTYPE html>
<html lang="en">
<head>
<meta charset="utf-8">
<title>Dr Megan Holt – Employment</title>
<link href="https://fonts.googleapis.com/css2?family=Roboto:wght@300;400;500&family=Roboto+Condensed:wght@400;700&display=swap" rel="stylesheet">
<style>
:root{
  --sage:#e0e3c3;
  --white:#ffffff;
  --orange:#e8870e;
  --ink:#555553;
  --ink-dark:#4a4a48;
  --rule:#8f8f86;
  --dots:#6e6e6e;
}
*{box-sizing:border-box;margin:0;padding:0}
html,body{width:1200px;height:778px;overflow:hidden}
body{background:var(--sage);font-family:"Roboto",sans-serif;color:var(--ink);position:relative}

.sidebar{position:absolute;left:0;top:0;width:188px;height:778px;background:var(--white);box-shadow:2px 0 8px rgba(0,0,0,.18)}
.brand-name{position:absolute;left:16px;top:76px;font-family:"Roboto",sans-serif;font-weight:400;font-size:20px;color:var(--ink-dark);white-space:nowrap}

.nav{position:absolute;left:16px;top:146px;width:156px;list-style:none}
.nav li{height:41.2px;display:flex;align-items:center;gap:8px;border-bottom:1px dotted var(--dots);font-size:10px;font-weight:400;letter-spacing:.1px;color:var(--ink-dark);text-transform:uppercase;white-space:nowrap}
.nav li.active{color:var(--orange)}
.nav svg{width:13px;height:12px;flex:none;fill:currentColor}

.social{position:absolute;left:15px;top:561px;display:flex;gap:4px}
.social span{width:27px;height:27px;border-radius:50%;background:var(--orange)}

.page-title{position:absolute;left:252px;top:146px;font-family:"Roboto Condensed",sans-serif;font-weight:700;font-size:32px;line-height:35px;text-transform:uppercase;color:var(--ink-dark)}
.page-title .accent{color:var(--orange)}

.scroll-hint{position:absolute;left:250px;top:496px;width:22px;height:90px}
.scroll-hint p{position:absolute;left:11px;top:32px;transform:translate(-50%,-50%) rotate(-90deg);font-size:13px;white-space:nowrap;color:var(--ink-dark)}
.scroll-hint svg{position:absolute;left:5px;top:72px}

.job{position:absolute;width:278px}
.job-year{display:flex;align-items:center;gap:13px;font-family:"Roboto Condensed",sans-serif;font-weight:700;font-size:14px;color:var(--orange);height:16px}
.job-year::after{content:"";flex:1;height:1px;background:var(--rule)}
.job-year.orange-rule::after{background:var(--orange)}
.job-place{margin-top:8px;font-family:"Roboto Condensed",sans-serif;font-weight:400;font-size:14.5px;text-transform:uppercase;color:var(--ink-dark);line-height:16px}
.job-role{font-family:"Roboto Condensed",sans-serif;font-weight:700;font-size:10px;text-transform:uppercase;color:var(--ink);line-height:12px}
.job-text{margin-top:10px;font-size:11.6px;font-weight:300;line-height:12.6px;color:var(--ink-dark)}
.job-text + .job-text{margin-top:12.6px}

.job--a{left:461px;top:149px}
.job--b{left:761px;top:149px}
.job--c{left:461px;top:391px}
.job--d{left:761px;top:391px}
</style>
</head>
<body>
<aside class="sidebar">
  <div class="brand-name">Dr Megan Holt</div>
  <ul class="nav">
    <li><svg viewBox="0 0 14 12"><path d="M7 0 0 6h2v6h4V8h2v4h4V6h2z"/></svg>Home</li>
    <li><svg viewBox="0 0 14 12"><circle cx="7" cy="3" r="3"/><path d="M1 12c0-4 3-5 6-5s6 1 6 5z"/></svg>About me</li>
    <li><svg viewBox="0 0 14 12"><circle cx="5" cy="6" r="3.5" fill="none" stroke="currentColor" stroke-width="2.5"/><circle cx="11" cy="3" r="2" fill="none" stroke="currentColor" stroke-width="1.6"/><circle cx="11" cy="9.5" r="1.8" fill="none" stroke="currentColor" stroke-width="1.6"/></svg>Skills</li>
    <li><svg viewBox="0 0 14 12"><path d="M5 1h4v2h4v9H1V3h4zM6 2v1h2V2z"/><path d="M6.2 5h1.6v1.6h1.6v1.6H7.8v1.6H6.2V8.2H4.6V6.6h1.6z" fill="#fff"/></svg>Professional experiences</li>
    <li><svg viewBox="0 0 14 12"><path d="M7 1 0 4l7 3 7-3z"/><path d="M3 6v3c2 2 6 2 8 0V6L7 8z"/></svg>Education</li>
    <li class="active"><svg viewBox="0 0 14 12"><path d="M2 0h10v12H8V9H6v3H2zM4 2v2h2V2zm4 0v2h2V2zM4 5v2h2V5zm4 0v2h2V5z"/></svg>Employment</li>
    <li><svg viewBox="0 0 14 12"><path d="M0 0h14v9H8v2h2v1H4v-1h2V9H0zm1.5 1.5v6h11v-6z"/></svg>My sites</li>
    <li><svg viewBox="0 0 14 12"><circle cx="7" cy="6" r="5.5"/></svg>Blog</li>
    <li><svg viewBox="0 0 14 12"><path d="M2 0h3l1 3-2 1.5c1 2 2 3 4 4L9.5 6.5l3 1v3C12 11.5 11 12 10 12 5 11.5 1 7.5 1 2 1 1 1.5 0 2 0z"/></svg>Contact</li>
  </ul>
  <div class="social" aria-label="Social links"><span></span><span></span></div>
</aside>

<h1 class="page-title">My<br><span class="accent">Employment</span></h1>

<div class="scroll-hint">
  <p>My sites</p>
  <svg width="12" height="16" viewBox="0 0 12 16"><path d="M6 0v13M2 9l4 5 4-5" fill="none" stroke="#4a4a48" stroke-width="1.8"/></svg>
</div>

<section class="job job--a">
  <div class="job-year">2005 - 2017</div>
  <h2 class="job-place">Well Spring Works</h2>
  <p class="job-role">Founder, Chiropractor</p>
  <p class="job-text">What a wonderful place to work! I can’t come to this clinic and not feel happy. It’s decorated for the hundreds of children who get treated here. I’ve been privileged to watch so many families blossoms through the stages of infancy to teens. They feel like family.</p>
  <p class="job-text">My job here as Chiropractor has been to train my Chiro­practic Associates, Chiropractic Assistants and support staff. To keep the standards high, the team managed and motivated, and the clinic excelling. In July 2016 I sold this business but I continue to work here as an Associate Chiropractor.</p>
</section>

<section class="job job--b">
  <div class="job-year">2004 - 2005</div>
  <h2 class="job-place">Harbour Point Spine &amp; Health Centre</h2>
  <p class="job-role">Associate Chiropractor</p>
  <p class="job-text">I learned a lot from my mentor Dr Daniel Ashford here. He taught me how to think like a business woman, which was exactly what I needed for my next move.</p>
</section>

<section class="job job--c">
  <div class="job-year orange-rule">2005 - 2004</div>
  <h2 class="job-place">Clear Balance Centre</h2>
  <p class="job-role">Associate Chiropractor</p>
  <p class="job-text">Working under Dr Graham Lowe has been the greatest gift I could have imagined first year out of University. He taught me his life’s learnings and I have treasured them. He taught me that the greatest gift for any teacher is to have their student surpass them. He taught me how to be an ego free teacher, share my knowledge unreservedly with those who ask, and how to life without expectations. He shaped me into the practitioner and teacher I have become.</p>
</section>

<section class="job job--d">
  <div class="job-year orange-rule">2002</div>
  <h2 class="job-place">Eastbrook University</h2>
  <p class="job-role">Chiropractic Skills Tutor and Examiner</p>
  <p class="job-text">What an honour to be invited to tutor and examine 2nd year Chiropractic Skills whilst in my final year of my Masters of Chiropractic. And what a delightful bunch of students we had that year too!</p>
</section>
</body>
</html>
```